Modern SaaS Dashboard Redesign for Building Management Platform

Overview:
Refer to pelvorn.com.au
We need a complete visual redesign of our property management dashboard to make it sleek, modern, and highly user-friendly. The current interface is functional but outdated. We want a high end SaaS design that feels intuitive, and visually engaging for daily use.

Style Direction:

Retain existing colour palette
Consistent, modern iconography and typography
Responsive design consideration (desktop-first, but adaptable to mobile)

Deliverables:
High-fidelity dashboard design in Figma or Adobe XD
Style guide for colours, typography, and icons
Layered files for developer handoff

Customer Journey Context

This dashboard is the central control panel for a property management SaaS platform (Pelvorn) used by building managers, strata managers, and executive committee members to manage building data and operations.

Entry Point: User logs in via the secure portal → lands directly on the dashboard.

Primary Goal: Quickly assess building portfolio health, upcoming actions, and key compliance dates.

Secondary Goal: Navigate smoothly to specific building data, reports, or contractor tasks without getting lost in menus.

Typical Flow:

Glance Phase (0–10 seconds) – User scans top stat cards for red/orange alerts or overdue actions.

Action Phase (10–30 seconds) – Clicks into urgent items from “Next Action List” or stat cards.

Work Phase (1–5 minutes) – Navigates to buildings or reports for detail work, filters/searches, and updates records.

2. Who This is For

Building Managers – Daily operational users, need fast visibility of inspections, insurance, defects, and maintenance.

Strata Managers / Property Managers – Portfolio-level oversight across multiple buildings.

Executive Committee Members (Owners Corporations) – View-only or limited-action users needing transparency and governance oversight.

Internal Support/Admin Staff – Back-office users providing data entry, compliance tracking, and troubleshooting.

3. Stakeholders Who Will See This Dashboard

Internal Admin Team – To monitor user activity and portfolio health.

Portfolio Managers – To track multiple properties at once and ensure compliance deadlines aren’t missed.

Building Service Providers – Certain contractors may have limited dashboard visibility for their assigned properties.

Compliance Officers / Auditors – May access the dashboard to verify documentation and timelines.

4. Key Design Considerations Based on Audience

Immediate clarity – Visual hierarchy that prioritises critical actions first.

Minimal learning curve – Clean, intuitive navigation with consistent patterns.

Quick search/filtering – Users may have dozens or hundreds of buildings to manage.

Mobile awareness – Many building managers work in the field, so components should adapt for tablets and smaller screens.

```html
<!DOCTYPE html>
<html lang="en">
<head>
<meta charset="utf-8">
<title>Pelvorn Dashboard</title>
<link href="https://fonts.googleapis.com/css2?family=Inter:wght@400;500;600;700&display=swap" rel="stylesheet">
<style>
:root{
  --bg:#171a35;
  --sidebar:#161931;
  --panel:#1f2346;
  --panel-2:#1a1e3d;
  --line:#3a3f6b;
  --active:#2b3163;
  --head:#262b55;
  --text:#ffffff;
  --dim:#7c81a5;
  --accent:#5b7cf5;
  --btn:#3a4383;
  --red:#ff4a5a;
  --orange:#f5a623;
  --green:#4fd1a5;
  --gray:#8f93b5;
}
*{box-sizing:border-box;margin:0;padding:0}
html,body{width:1200px;height:467px;overflow:hidden;background:var(--bg);font-family:"Inter",sans-serif;color:var(--text)}
.app{position:relative;width:1200px;height:467px}
.sidebar{position:absolute;left:0;top:0;width:151px;height:467px;background:var(--sidebar);border-right:1px solid var(--line)}
.brand{position:absolute;left:14px;top:16px;display:flex;align-items:center;gap:6px;font-weight:700;font-size:14px}
.brand .dot{width:14px;height:14px;border-radius:50%;background:#fff}
.nav{position:absolute;left:14px;top:58px;width:123px;list-style:none}
.nav li{display:flex;align-items:center;gap:8px;padding:0 5px;height:28.5px;font-size:9px;font-weight:600;line-height:1.15}
.nav li.active{background:var(--active);border-radius:4px;height:24px;margin-bottom:4px}
.nav li.tall{height:34px}
.nav svg{width:13px;height:13px;flex:none;stroke:#fff;fill:none;stroke-width:1.5}
.search{position:absolute;left:170px;top:12px;width:670px;height:32px;background:var(--panel);border-radius:5px;display:flex;align-items:center;padding-left:18px;gap:10px;font-size:8.5px;color:#dcdef0}
.search svg{width:10px;height:10px;stroke:#ccc;fill:none;stroke-width:1.6}
.profile{position:absolute;left:1020px;top:14px;display:flex;align-items:center;gap:8px}
.profile .dot{width:18px;height:18px;border-radius:50%;background:#fff}
.profile .name{font-size:15px;font-weight:500;display:flex;align-items:center;gap:6px}
.profile .name svg{width:9px;height:9px;stroke:var(--accent);fill:none;stroke-width:1.8}
.profile .mail{font-size:9px;margin-top:2px}
.topline{position:absolute;left:151px;right:0;top:56px;border-top:1px solid var(--line)}
.stats{position:absolute;left:170px;top:70px;display:flex;gap:11px}
.stat{width:159px;height:95px;background:var(--panel);border-radius:5px;padding:11px 10px}
.tag{display:block;width:126px;height:12px;border-radius:6px;border:1px solid #3a3f6b;background:#14172e;font-size:7.5px;padding:0 6px;line-height:11px}
.tag.red{color:var(--red);border-color:#5a2a3a}
.tag.orange{color:var(--orange)}
.tag.gray{color:var(--gray)}
.tag.green{color:var(--green)}
.stat .num{font-size:17.5px;font-weight:600;margin-top:8px}
.stat .label{font-size:8.5px;font-weight:500;margin-top:5px}
.stat .sub{font-size:7px;margin-top:7px;color:#dfe1f0}
.panel{position:absolute;background:var(--panel);border-radius:6px}
.buildings{left:170px;top:177px;width:670px;height:272px;padding:11px 10px}
h2{font-size:15px;font-weight:600}
.tabs{display:flex;gap:8px;margin-top:9px}
.tabs span{font-size:9.5px;padding:0 8px;height:18px;line-height:16px;border:1px solid var(--line);border-radius:3px}
.tabs span.on{background:var(--accent);border-color:var(--accent)}
.filters{display:flex;gap:14px;margin-top:13px;align-items:flex-end}
.field label{display:block;font-size:7.8px;margin-bottom:4px}
.field .box{width:108px;height:23px;border:1px solid var(--line);border-radius:3px;font-size:9.5px;color:var(--dim);padding-left:11px;line-height:21px;position:relative}
.field .box.sel{color:#fff;width:95px}
.field.mgr .box{width:94px}
.field .box svg{position:absolute;right:8px;top:7px;width:9px;height:7px;stroke:#fff;fill:none;stroke-width:1.5}
.filter-btn{width:62px;height:23px;background:var(--accent);border-radius:3px;font-size:9.5px;text-align:center;line-height:23px;font-weight:500;margin-left:2px}
.table{margin-top:19px;border:1px solid var(--line);border-radius:5px;overflow:hidden}
table{width:100%;border-collapse:collapse;font-size:9.5px}
th{background:var(--head);font-weight:400;text-align:left;height:27px;padding:0 5px;line-height:1.15}
td{height:36px;padding:0 5px;border-top:1px solid var(--line);line-height:1.2;vertical-align:middle;font-weight:400}
td.num{vertical-align:top;padding-top:9px}
.pill{display:inline-block;font-size:7px;padding:3px 5px;border-radius:2px;border:1px solid}
.pill.due{color:var(--orange);border-color:var(--orange);background:#3a2f2a}
.pill.ok{color:var(--green);border-color:#3d6a73;background:#1f3a48;padding:3px 8px}
.pill.over{color:var(--red);border-color:var(--red);background:#3a1e2e}
.acts{display:flex;gap:6px}
.acts i{width:12px;height:12px;background:#121530;border-radius:2px;display:flex;align-items:center;justify-content:center}
.acts svg{width:7px;height:7px;stroke:#fff;fill:none;stroke-width:1.4}
.actions{left:851px;top:177px;width:329px;height:214px;padding:11px 10px}
.item{border:1px solid var(--line);border-radius:5px;background:var(--panel-2);margin-top:8px;padding:9px 10px;position:relative;height:46px}
.item.tall{height:56px}
.item .t{font-size:9px;font-weight:400;width:170px;line-height:1.2}
.item .m{font-size:7px;color:var(--dim);margin-top:4px;display:flex;align-items:center;gap:5px}
.lvl{font-size:7px;padding:2px 5px;border:1px solid;border-radius:2px}
.lvl.high{color:var(--red);border-color:var(--red);background:#3a1e2e}
.lvl.med{color:var(--orange);border-color:var(--orange);background:#3a2f2a}
.lvl.low{color:var(--green);border-color:#3d6a73;background:#1f3a48}
.btns{position:absolute;right:10px;top:15px;display:flex;gap:6px}
.item.tall .btns{top:16px}
.btns span{font-size:6px;height:16px;line-height:16px;padding:0 5px;border-radius:2px;background:var(--btn);border:1px solid #5a63a8}
.btns span.go{background:var(--accent);border-color:var(--accent)}
</style>
</head>
<body>
<div class="app">
  <aside class="sidebar">
    <div class="brand"><span class="dot"></span>Pelvorn</div>
    <ul class="nav">
      <li class="active"><svg viewBox="0 0 16 16"><path d="M2 7l6-5 6 5v7H2z"/><path d="M6 14v-4h4v4"/></svg>Buildings</li>
      <li class="tall"><svg viewBox="0 0 16 16"><path d="M2 3h5v11H2zM9 3h5v11H9z"/></svg>Contractors Address Book</li>
      <li><svg viewBox="0 0 16 16"><rect x="2" y="2" width="12" height="12"/><path d="M2 6h12M6 6v8"/></svg>Report Builder</li>
      <li><svg viewBox="0 0 16 16"><ellipse cx="8" cy="4" rx="5" ry="2"/><path d="M3 4v8c0 1 2 2 5 2s5-1 5-2V4M3 8c0 1 2 2 5 2s5-1 5-2"/></svg>Management Data</li>
      <li><svg viewBox="0 0 16 16"><rect x="3" y="2" width="10" height="12"/><path d="M5 6h6M5 9h6M5 12h4"/></svg>Email Log Report</li>
      <li><svg viewBox="0 0 16 16"><circle cx="8" cy="5" r="3"/><path d="M2 15c0-4 3-5 6-5s6 1 6 5"/></svg>Administration</li>
      <li><svg viewBox="0 0 16 16"><circle cx="8" cy="8" r="6"/><path d="M6 6c0-2 4-2 4 0 0 1-2 1-2 3M8 11v1"/></svg>About Us + Support</li>
      <li><svg viewBox="0 0 16 16"><rect x="3" y="2" width="10" height="12"/><path d="M5 6h6M5 9h6"/></svg>Training Hub</li>
    </ul>
  </aside>

  <div class="search"><svg viewBox="0 0 12 12"><circle cx="5" cy="5" r="3.5"/><path d="M8 8l3 3"/></svg>Search buildings, reports, contractors...</div>
  <div class="profile">
    <span class="dot"></span>
    <div>
      <div class="name">Pelvorn <svg viewBox="0 0 10 8"><path d="M1 2l4 4 4-4"/></svg></div>
      <div class="mail">admin@pelvornportal.com</div>
    </div>
  </div>
  <div class="topline"></div>

  <section class="stats">
    <div class="stat"><span class="tag red">Overdue</span><div class="num">8</div><div class="label">OPEN MAINTENANCE</div><div class="sub">+2 this week</div></div>
    <div class="stat"><span class="tag orange">Pending</span><div class="num">10</div><div class="label">UPCOMING INSPECTIONS</div><div class="sub">20 days left</div></div>
    <div class="stat"><span class="tag orange">Pending</span><div class="num">6</div><div class="label">INSURANCE RENEWALS</div><div class="sub">5 expire soon</div></div>
    <div class="stat"><span class="tag gray">Portfolio</span><div class="num">82</div><div class="label">BUILDINGS</div><div class="sub">1 with alerts</div></div>
    <div class="stat"><span class="tag gray">Portfolio</span><div class="num">12</div><div class="label">NEXT ACTIONS</div><div class="sub">3 high priority</div></div>
    <div class="stat"><span class="tag green">Healthy</span><div class="num">94%</div><div class="label">COMPLIANCE SCORE</div><div class="sub">+1% from last month</div></div>
  </section>

  <section class="panel buildings">
    <h2>Buildings</h2>
    <div class="tabs"><span class="on">All</span><span>Overdue</span><span>Expiring Soon</span><span>Active</span><span>Archived</span></div>
    <div class="filters">
      <div class="field"><label>Units Plan No.</label><div class="box">Units Plan No.</div></div>
      <div class="field"><label>Building Name</label><div class="box">Search name</div></div>
      <div class="field"><label>Suburb</label><div class="box">Start typing...</div></div>
      <div class="field mgr"><label>Manager</label><div class="box sel">Any<svg viewBox="0 0 10 7"><path d="M1 1l4 4 4-4"/></svg></div></div>
      <div class="field"><label>Status</label><div class="box sel">Active<svg viewBox="0 0 10 7"><path d="M1 1l4 4 4-4"/></svg></div></div>
      <div class="filter-btn">FILTER</div>
    </div>
    <div class="table">
      <table>
        <thead><tr><th style="width:59px">UP No.</th><th style="width:94px">Building</th><th style="width:77px">Group</th><th style="width:84px">Address</th><th style="width:75px">Suburb</th><th style="width:69px">Manager</th><th style="width:53px">Live<br>Posts</th><th style="width:81px">Renewals</th><th>Action</th></tr></thead>
        <tbody>
          <tr><td>UPM-<br>1123</td><td>Pelvorn Towers</td><td>Test Group<br>A</td><td>56 Harlow<br>Lane</td><td>Ashvale</td><td>Mira Colt</td><td class="num">0</td><td><span class="pill due">Due 30 Jun</span></td><td><div class="acts"><i><svg viewBox="0 0 8 8"><path d="M1 7l1-2 4-4 1 1-4 4z"/></svg></i><i><svg viewBox="0 0 8 8"><path d="M1 4l2 2 4-4"/></svg></i><i><svg viewBox="0 0 8 8"><path d="M1 2h6M2 2v5h4V2M3 1h2"/></svg></i></div></td></tr>
          <tr><td>UPM-<br>1459</td><td>C2 Corvan</td><td>Test Group<br>B</td><td>49 Dunmore<br>Street</td><td>Kestin</td><td>Tobias<br>Rell</td><td>7</td><td><span class="pill ok">Ok</span></td><td><div class="acts"><i><svg viewBox="0 0 8 8"><path d="M1 7l1-2 4-4 1 1-4 4z"/></svg></i><i><svg viewBox="0 0 8 8"><path d="M1 4l2 2 4-4"/></svg></i><i><svg viewBox="0 0 8 8"><path d="M1 2h6M2 2v5h4V2M3 1h2"/></svg></i></div></td></tr>
          <tr><td>UPM-<br>1460</td><td>Halden Block<br>A</td><td>Test Group<br>C</td><td>11 Quarry<br>Street</td><td>Brindle</td><td>Tobias<br>Rall</td><td>0</td><td><span class="pill over">Overdue</span></td><td><div class="acts"><i><svg viewBox="0 0 8 8"><path d="M1 7l1-2 4-4 1 1-4 4z"/></svg></i><i><svg viewBox="0 0 8 8"><path d="M1 4l2 2 4-4"/></svg></i><i><svg viewBox="0 0 8 8"><path d="M1 2h6M2 2v5h4V2M3 1h2"/></svg></i></div></td></tr>
        </tbody>
      </table>
    </div>
  </section>

  <section class="panel actions">
    <h2>Next Action List</h2>
    <div class="item">
      <div class="t">Book routine inspection – Corvan C2</div>
      <div class="m">Due: 26 Jun 2025 Contact: Mira Colton <span class="lvl high">High</span></div>
      <div class="btns"><span>View</span><span>Assign</span><span class="go">Complete</span></div>
    </div>
    <div class="item tall">
      <div class="t">Upload insurance certificate – Pelvorn Towers</div>
      <div class="m">Due: 30 Jun 2025 Owner: Compliance <span class="lvl med">Medium</span></div>
      <div class="btns"><span>View</span><span>Assign</span><span class="go">Complete</span></div>
    </div>
    <div class="item">
      <div class="t">Defect follow-up – Lobby lighting</div>
      <div class="m">Due: 2 Jul 2025 Contractor: Lumenwork <span class="lvl low">Low</span></div>
      <div class="btns"><span>View</span><span>Assign</span><span class="go">Complete</span></div>
    </div>
  </section>
</div>
</body>
</html>
```